Corvella Flood Restoration needing website

Hi Team

We are looking for a 4 or 5 page website containing
1: Home
2: Services
3: Gallery
4: Equipment Hire
5 Contact Us

Would want the front page to be a big call to action. Someones house has just flooded...they're highly stressed and we just want to let them know straight away that we can assist them

Some call to action would be great.

"Wet Carpets??"

"Washing machine just overflowed??"

"Burst pipe?"

"We're here to help!!"

Would be wanting a scrolling banner type homepage with images of flooded houses, heavy rain, a mother in shock that the house has been flooded by an overflowing washing machine, someone taking an emergency call with text saying that we are there to take your call 24/7 365 days a year

Target Market(s)

insurance companies and home owners

Industry/Entity Type

Hire

Coding

Coded - Design and coding required

Number of Pages Required

5+ page

Requirements
Must have
• 24/7 emergency contact number on home page (0468215937)
• 4 photos on banner on home page
• Equipment Hire Page should include images and brief description of these 3 products
• http://www.brintagesupply.com.au/item574.htm
• http://www.valdrix-tools.com.au/product/fresh-gust-fanunit/
• http://www.strellon.com.au/carpet/carpet-extractor-nomad-ser-i-ser-ii-ser-iii
• SERVICES OFFERED ARE:
• 24/7 Emergnecy Flood Restoration
• Insurance Claims
• Structural Drying
• Sub Floor Drying
• Supply and installation of drying equipment
• Professional Carpet and underlay installation
Nice to have
• Some other websites we like
• www.quillbyleakcare.com.au
• www.harrowdenrepairservices.com.au/flood-water-damage-restoration
• http://www.pelmarrecovery.com.au/
• http://www.drywellremedygroup.com.au/
Should not have
• not looking for an all white background.

```html
<!DOCTYPE html>
<html lang="en">
<head>
<meta charset="utf-8">
<title>Corvella Flood Restoration</title>
<link href="https://fonts.googleapis.com/css2?family=Open+Sans:ital,wght@0,400;0,600;0,700;0,800;1,700;1,800&family=Cinzel:wght@700&display=swap" rel="stylesheet">
<style>
:root{
  --blue:#1795d4;
  --blue-dark:#0f6fa6;
  --blue-light:#7fc8ec;
  --navy:#0e3f6b;
  --orange:#f7941d;
  --gray:#8a8a8a;
  --gray-dark:#6f6f6f;
  --ink:#222;
  --white:#fff;
  --black:#0c0c0c;
}
*{box-sizing:border-box;margin:0;padding:0}
html,body{width:1200px;height:4534px;overflow:hidden}
body{font-family:"Open Sans",Arial,sans-serif;color:var(--ink);background:var(--white);position:relative}
section,header,nav,footer{position:absolute;left:0;width:1200px}
.heading{font-family:"Cinzel",Georgia,serif;font-weight:700;font-size:40px;line-height:50px;color:var(--white);text-align:center;letter-spacing:1px}
.btn{display:inline-block;font-family:"Cinzel",Georgia,serif;font-weight:700;font-size:13px;letter-spacing:1px;text-align:center}
.lead{color:var(--white);font-size:13.5px;line-height:20px;text-align:center;font-weight:400}
.pointer{position:absolute;left:585px;bottom:-20px;width:0;height:0;border-left:15px solid transparent;border-right:15px solid transparent;border-top:20px solid var(--gray);z-index:2}

/* header */
.site-header{top:0;height:120px;background:var(--white)}
.brand{position:absolute;left:105px;top:26px;display:flex;align-items:center;gap:14px}
.brand-mark{width:28px;height:28px;background:var(--blue)}
.brand-name{font-weight:800;font-size:30px;line-height:34px;color:var(--navy);text-transform:uppercase;letter-spacing:1px}
.emergency{position:absolute;right:100px;top:24px;display:flex;align-items:center;gap:10px}
.emergency-icon{width:66px;height:66px;border-radius:50%;background:var(--orange)}
.emergency small{display:block;font-size:14px;font-weight:700;color:var(--ink)}
.emergency strong{display:block;font-size:40px;line-height:42px;font-weight:800;color:var(--orange)}

/* nav */
.main-nav{top:120px;height:37px;background:var(--blue);display:flex;align-items:center;padding-left:100px}
.main-nav a{color:var(--white);text-decoration:none;font-weight:700;font-size:13px;text-transform:uppercase;padding:0 22px;line-height:37px}
.main-nav a.active{background:#9fc3d8;color:var(--navy)}
.social{position:absolute;right:100px;top:9px;display:flex;gap:6px}
.social span{width:20px;height:20px;background:var(--white);border-radius:3px}

/* hero */
.hero{top:157px;height:568px}
.hero-photo{position:absolute;inset:0;background:linear-gradient(180deg,#b9b6ae 0%,#8d8a84 45%,#6e7880 70%,#9aa3a8 100%)}
.slide-title{position:absolute;left:250px;top:488px;width:655px;height:80px;background:linear-gradient(90deg,#2fa3dc,#8fd0f0);color:var(--white);font-weight:800;font-style:italic;font-size:30px;line-height:80px;padding-left:30px}
.slide-enquiry{position:absolute;left:905px;top:488px;width:295px;height:80px;background:var(--orange);color:var(--white);font-weight:700;font-size:22px;line-height:80px;padding-left:45px}

/* welcome */
.welcome{top:725px;height:470px;background:var(--gray)}
.welcome .heading{margin-top:75px}
.welcome .lead{width:1000px;margin:35px auto 0}
.btn-outline{display:block;width:220px;margin:30px auto 0;border:2px solid var(--white);border-radius:5px;color:var(--white);padding:10px 0}

/* services */
.services{top:1195px;height:710px;background:var(--blue)}
.services .heading{margin-top:110px}
.service-grid{position:absolute;left:100px;top:190px;width:1000px;display:grid;grid-template-columns:490px 490px;column-gap:20px;row-gap:25px}
.service-card{background:var(--white);height:140px;display:flex;position:relative}
.service-photo{width:175px;height:140px;flex:none}
.service-body{padding:14px 16px}
.service-body h3{font-size:13px;font-weight:800;margin-bottom:6px}
.service-body p{font-size:10.5px;line-height:14px;color:#444}
.service-actions{position:absolute;right:0;bottom:0;display:flex}
.service-actions span{font-size:11px;font-weight:700;color:var(--white);padding:5px 16px}
.more{background:var(--blue)}
.enquire{background:var(--orange)}

/* emergency band */
.emergency-band{top:1905px;height:310px;background:var(--blue-light)}
.emblem{position:absolute;left:100px;top:45px;width:220px;height:220px;border-radius:50%;background:#4ea9d6}
.emergency-band h2{position:absolute;left:355px;top:60px;color:var(--white);font-weight:800;font-style:italic;font-size:30px}
.emergency-band h2 em{font-size:28px}
.emergency-band p{position:absolute;left:355px;top:110px;width:745px;color:var(--white);font-size:14px;line-height:21px;font-weight:400}

/* gallery */
.gallery{top:2215px;height:625px;background:linear-gradient(180deg,#2c3236,#1b1f22 60%,#262b2f)}
.gallery .heading{margin-top:110px}
.gallery-grid{position:absolute;left:100px;top:177px;width:1000px;display:grid;grid-template-columns:repeat(5,192px);gap:10px}
.gallery-grid div{height:128px}
.btn-light{position:absolute;left:495px;top:470px;width:210px;background:var(--white);color:var(--ink);border-radius:5px;padding:10px 0}

/* equipment */
.equipment{top:2840px;height:665px;background:var(--gray)}
.equipment .heading{margin-top:110px}
.equipment-grid{position:absolute;left:100px;top:170px;display:flex;gap:28px}
.equipment-card{width:315px;height:395px;background:var(--white);border-radius:10px;text-align:center;padding:15px}
.equipment-photo{height:240px;border-radius:4px}
.equipment-card h3{font-size:13px;font-weight:800;margin:18px 0 6px}
.equipment-card p{font-size:11px;line-height:15px;color:#333}
.btn-small{margin-top:10px;border:1.5px solid var(--ink);border-radius:4px;font-size:10px;padding:5px 14px;color:var(--ink)}

/* contact */
.contact{top:3505px;height:600px;background:var(--blue)}
.contact .heading{margin-top:110px}
.contact .lead{width:1000px;margin:18px auto 0}
.field{position:absolute;left:100px;width:315px;height:40px;background:var(--white);color:#888;font-size:12px;padding:12px 10px;border:1px solid #d7e7f0}
.message{position:absolute;left:425px;top:265px;width:675px;height:170px;background:var(--white);color:#888;font-size:12px;padding:10px}
.btn-send{position:absolute;left:490px;top:455px;width:220px;background:var(--orange);color:var(--white);border-radius:8px;padding:16px 0;font-size:14px}

/* footer */
.site-footer{top:4105px;height:429px;background:var(--black);color:#bbb}
.footer-brand{position:absolute;left:100px;top:120px;width:230px;text-align:center;display:flex;flex-direction:column;align-items:center;gap:12px}
.footer-brand .brand-mark{background:#9a9a9a;width:40px;height:40px}
.footer-brand span{font-weight:800;font-size:22px;line-height:26px;color:#9a9a9a;text-transform:uppercase}
.footer-col{position:absolute;top:40px;width:235px}
.footer-col h4{font-family:"Cinzel",Georgia,serif;font-size:14px;color:#ccc;padding-bottom:8px;border-bottom:1px solid #555;margin-bottom:6px}
.footer-col li{list-style:none;font-size:12px;line-height:16px;padding:10px 0 10px 14px;border-bottom:1px solid #2b2b2b;position:relative}
.footer-col li::before{content:"›";position:absolute;left:2px;color:var(--orange)}
.contact-line{font-size:12px;padding:6px 0;display:flex;gap:8px}
.contact-line b{color:var(--orange)}
.footer-social{display:flex;gap:6px;margin:14px 0}
.footer-social span{width:24px;height:24px;background:#aaa;border-radius:3px}
.btn-enquiry{background:var(--orange);color:var(--white);border-radius:5px;padding:9px 22px;font-size:12px}
.copyright{position:absolute;left:0;bottom:0;width:1200px;height:34px;background:#1b1b1b;font-size:11px;line-height:34px;text-align:center;color:#999}
</style>
</head>
<body>

<header class="site-header">
  <div class="brand"><span class="brand-mark"></span><span class="brand-name">Corvella<br>Flood Restoration</span></div>
  <div class="emergency">
    <div class="emergency-icon" role="img" aria-label="Emergency phone badge"></div>
    <div><small>Emergency Contact</small><strong>0468215937</strong></div>
  </div>
</header>

<nav class="main-nav">
  <a class="active">Home</a><a>Services</a><a>Gallery</a><a>Equipment Hire</a><a>Contact Us</a>
  <div class="social"><span></span><span></span><span></span></div>
</nav>

<section class="hero">
  <div class="hero-photo" role="img" aria-label="Flooded home interior with water across the floor below a staircase"></div>
  <div class="slide-title">The Slider Title Goes Here</div>
  <div class="slide-enquiry">ENQUIRY »</div>
</section>

<section class="welcome">
  <h2 class="heading">WELCOME</h2>
  <p class="lead">Lorem ipsum dolor sit amet, consectetur adipiscing elit. Duis ultricies aliquet risus, a facilisis tortor pulvinar posuere. Suspendisse in augue et felis rhoncus consectetur. Etiam tincidunt pulvinar dui at porta. Cras a facilisis diam. Sed auctor justo eu neque pellentesque porta. Morbi quis imperdiet ex. Aenean varius a massa a eleifend. Sed eros lorem, dictum id cursus pellentesque, vulputate non augue. Mauris luctus quam a fermentum consequat. Nunc vel malesuada elit. Fusce tincidunt sed et id fermentum. Nulla tincidunt feugiat diam id luctus. In consequat risus et sapien efficitur, vel ultricies metus commodo. Donec sem enim, consequat nec lacinia id, tristique et nisi. Pellentesque non fringilla velit. Suspendisse potenti. Curabitur maximus lorem dolor, et ullamcorper velit semper sed. Vivamus in arcu ut orci efficitur ornare rhoncus et odio interdum et malesuada fames ac ante ipsum primis in faucibus. Pellentesque tincidunt nisi posuere nunc lacinia, at sollicitudin risus volutpat. Ut dapibus tellus vitae semper rhoncus donec faucibus quam et luctus vulputate. Quisque sit amet interdum velit. Suspendisse pharetra justo non mattis aliquam praesent bibendum mauris a nisl feugiat.</p>
  <span class="btn btn-outline">LEARN WHAT WE DO »</span>
  <span class="pointer"></span>
</section>

<section class="services">
  <h2 class="heading">SERVICES</h2>
  <div class="service-grid">
    <article class="service-card">
      <div class="service-photo" role="img" aria-label="Flooded street with water in front of a house" style="background:linear-gradient(135deg,#6d8fa0,#3e5f6c)"></div>
      <div class="service-body"><h3>24/7 Emergency Flood Restoration</h3><p>Lam tincidunt pulvinar dui at porta cras a facilisis diam sed auctor justo eu neque pellentesque porta. Morbi quis imperdiet ex aenean varius a massa a eleifend sed eros lorem, dictum id cursus pellentesque vulputate.</p></div>
      <div class="service-actions"><span class="more">MORE »</span><span class="enquire">ENQUIRE »</span></div>
    </article>
    <article class="service-card">
      <div class="service-photo" role="img" aria-label="Assessors inspecting a flood damaged home for an insurance claim" style="background:linear-gradient(135deg,#8d8e88,#4f5250)"></div>
      <div class="service-body"><h3>Insurance Claims</h3><p>Proin iaculis, quam nec congue sodales, ante nisl suscipit nisl, eu efficitur leo justo id mauris. Phasellus dapibus faucibus nisl, non hendrerit sapien luctus et. Sed venenatis libero aliquam ullamcorper sollicitudin.</p></div>
      <div class="service-actions"><span class="more">MORE »</span><span class="enquire">ENQUIRE »</span></div>
    </article>
    <article class="service-card">
      <div class="service-photo" role="img" aria-label="Yellow drying fan on a floor" style="background:linear-gradient(135deg,#d9c64a,#6b6a55)"></div>
      <div class="service-body"><h3>Structural Drying</h3><p>In ultricies finibus ex dapibus fermentum ut sodales hendrerit felis, non vestibulum mi varius sollicitudin. Sed bibendum, augue eu scelerisque fermentum, mi arcu elementum ligula, sit amet laoreet nisl lacus.</p></div>
      <div class="service-actions"><span class="more">MORE »</span><span class="enquire">ENQUIRE »</span></div>
    </article>
    <article class="service-card">
      <div class="service-photo" role="img" aria-label="Drying equipment under a raised timber floor" style="background:linear-gradient(135deg,#6a6e72,#2d3033)"></div>
      <div class="service-body"><h3>Sub Floor Drying</h3><p>Magna elit gravida turpis, eget dignissim nisi enim eu diam. Vivamus molestie in metus vitae vehicula aliquam ultricies, justo quis efficitur tincidunt, quam leo pellentesque erat, a molestie lorem nisi vitae purus.</p></div>
      <div class="service-actions"><span class="more">MORE »</span><span class="enquire">ENQUIRE »</span></div>
    </article>
    <article class="service-card">
      <div class="service-photo" role="img" aria-label="Drying machine placed on a wet floor" style="background:linear-gradient(135deg,#b2b0aa,#5b5a56)"></div>
      <div class="service-body"><h3>Supply &amp; Installation of Drying Equipment</h3><p>Duis ultricies nulla ac tortor laoreet fermentum. Aliquam egestas, tellus et efficitur sagittis, urna justo feugiat elit, sit amet tincidunt tellus neque vel nisi. Pellentesque mollis purus et turpis finibus porttitor.</p></div>
      <div class="service-actions"><span class="more">MORE »</span><span class="enquire">ENQUIRE »</span></div>
    </article>
    <article class="service-card">
      <div class="service-photo" role="img" aria-label="Hands laying new carpet with a tool" style="background:linear-gradient(135deg,#7fb6c6,#c9c4b8)"></div>
      <div class="service-body"><h3>Professional Carpet &amp; Underlay Installation</h3><p>Nunc tincidunt erat et lorem tristique porta maecenas malesuada feugiat augue. Vestibulum vel diam quis nibh auctor pretium et ac ante. Vestibulum sed quam in faucibus orci luctus et ultrices posuere cubilia.</p></div>
      <div class="service-actions"><span class="more">MORE »</span><span class="enquire">ENQUIRE »</span></div>
    </article>
  </div>
</section>

<section class="emergency-band">
  <div class="emblem" role="img" aria-label="Round 24/7 emergency phone emblem"></div>
  <h2>24/7 EMERGENCY SERVICE: <em>call us 0468215937</em></h2>
  <p>Lorem ipsum dolor sit amet, consectetur adipiscing elit. Duis ultricies aliquet risus, a facilisis tortor pulvinar posuere. Suspendisse in augue et felis rhoncus consectetur. Etiam tincidunt pulvinar dui at porta. Cras a facilisis diam. Sed auctor justo eu neque pellentesque porta. Morbi quis imperdiet ex. Aenean varius a massa a eleifend. Sed eros lorem, dictum id cursus pellentesque, vulputate non augue. Mauris luctus quam a fermentum consequat. Nunc vel malesuada elit. Id fermentum ultrices feugiat diam id luctus. In consequat risus et sapien efficitur, vel ultricies metus commodo. Donec sem enim, consequat nec lacinia id, tristique et nisi.</p>
</section>

<section class="gallery">
  <h2 class="heading">GALLERY</h2>
  <div class="gallery-grid">
    <div role="img" aria-label="Sandbags stacked in a flooded room" style="background:linear-gradient(135deg,#8a7358,#4a3a2c)"></div>
    <div role="img" aria-label="Flooded road with a warning sign" style="background:linear-gradient(135deg,#8c9a9c,#c9524a)"></div>
    <div role="img" aria-label="Clean restored living room" style="background:linear-gradient(135deg,#d8d7d2,#9a9891)"></div>
    <div role="img" aria-label="Worker cleaning a flooded floor" style="background:linear-gradient(135deg,#c7c8c2,#5f7b8a)"></div>
    <div role="img" aria-label="Water damaged kitchen floor" style="background:linear-gradient(135deg,#b49a7a,#6c4f3b)"></div>
    <div role="img" aria-label="Bright interior after restoration" style="background:linear-gradient(135deg,#e6d9a8,#a99660)"></div>
    <div role="img" aria-label="Water leaking onto a floor" style="background:linear-gradient(135deg,#d4dde2,#7d8f99)"></div>
    <div role="img" aria-label="Houses surrounded by flood water" style="background:linear-gradient(135deg,#9a8c78,#5c6a6e)"></div>
    <div role="img" aria-label="Large drying fan" style="background:linear-gradient(135deg,#6d6a66,#2b2a28)"></div>
    <div role="img" aria-label="Boots wading through flooded floor" style="background:linear-gradient(135deg,#cfc9bd,#8b8172)"></div>
  </div>
  <span class="btn btn-light">VIEW ALL PHOTOS »</span>
</section>

<section class="equipment">
  <h2 class="heading">EQUIPMENT HIRE</h2>
  <div class="equipment-grid">
    <article class="equipment-card">
      <div class="equipment-photo" role="img" aria-label="Blue portable dehumidifier unit" style="background:linear-gradient(160deg,#f3f6f8,#4aa6d4 55%,#2b6f92)"></div>
      <h3>DEHUMIDIFIER DX 2500 230VOLT</h3>
      <p>Lam tincidunt pulvinar dui at porta. Cras a facilisis diam. Sed auctor justo eu neque pellentesque porta. Morbi quis imperdiet ex. Aenean varius a massa a eleifend.</p>
      <span class="btn btn-small">LEARN MORE »</span>
    </article>
    <article class="equipment-card">
      <div class="equipment-photo" role="img" aria-label="Blue stacked air mover fans" style="background:linear-gradient(160deg,#f3f6f8,#2f5fc2 55%,#1c3a7c)"></div>
      <h3>Fresh Gust Fanunit</h3>
      <p>Sed eros lorem, dictum id cursus pellentesque vulput ate non augue. Mauris luctus quam a fermentum consequat nunc vel malesuada elit fusce tincidunt sed.</p>
      <span class="btn btn-small">LEARN MORE »</span>
    </article>
    <article class="equipment-card">
      <div class="equipment-photo" role="img" aria-label="White and red carpet extractor machine" style="background:linear-gradient(160deg,#f6f6f6,#d9d9d9 55%,#b84a3c)"></div>
      <h3>Carpet Extractor - Nomad Ser II, Ser III</h3>
      <p>Donec rutrum ligula quis, eget auctor velit cursus et. Suspendisse sollicitudin tristique risus ut maximus. Aenean velit est, lacinia vel interdum at cursus vitae.</p>
      <span class="btn btn-small">LEARN MORE »</span>
    </article>
  </div>
</section>

<section class="contact">
  <h2 class="heading">CONTACT US</h2>
  <p class="lead">Lorem ipsum dolor sit amet, consectetur adipiscing elit. Duis ultricies aliquet risus, a facilisis tortor pulvinar posuere. Suspendisse in augue et felis rhoncus consectetur. Etiam tincidunt pulvinar dui at porta. Cras a facilisis diam. Sed auctor justo eu neque pellentesque porta. Morbi quis imperdiet ex. Aenean varius a massa a eleifend. Sed eros lorem, dictum id cursus pellentesque, vulputate non augue.</p>
  <div class="field" style="top:265px">Name</div>
  <div class="field" style="top:308px">Email</div>
  <div class="field" style="top:351px">Phone</div>
  <div class="field" style="top:394px">Subject</div>
  <div class="message">Message</div>
  <span class="btn btn-send">SEND A MESSAGE »</span>
</section>

<footer class="site-footer">
  <div class="footer-brand"><span class="brand-mark"></span><span>Corvella<br>Flood Restoration</span></div>
  <div class="footer-col" style="left:355px">
    <h4>LINKS</h4>
    <ul><li>Home</li><li>Services</li><li>Gallery</li><li>Equipment Hire</li><li>Contact Us</li><li>Privacy</li></ul>
  </div>
  <div class="footer-col" style="left:610px">
    <h4>SERVICES</h4>
    <ul><li>24/7 Emergency Flood Restoration</li><li>Insurance Claims</li><li>Structural Drying</li><li>Sub Floor Drying</li><li>Supply &amp; Installation of Drying Equipment</li><li>Professional Carpet &amp; Underlay Installation</li></ul>
  </div>
  <div class="footer-col" style="left:865px">
    <h4>GET IN TOUCH</h4>
    <div class="contact-line"><b>P:</b> 0468215937</div>
    <div class="contact-line"><b>E:</b> info@corvellafloodrestoration.com</div>
    <div class="contact-line"><b>A:</b> 48 Larkin Street<br>Sydney NSW 2000</div>
    <div class="footer-social"><span></span><span></span><span></span></div>
    <span class="btn btn-enquiry">ENQUIRY »</span>
  </div>
  <div class="copyright">©2020 Corvella Flood Restoration</div>
</footer>

</body>
</html>
```